Design Business Card Aerial Drone Photography

we need a business card that shows we are a leader in:
-Aerial Videos
-Aerial Photography
-Aerial Real Estate Photography
the attached logo is in blue, however please feel free to submit creative colors and designs
Updates

I would like to add the words "Veteran Owned and Operated" to my business card Certified Drone Operator should appear as one line Thanks, Ray Colton

Target Market(s)

real estate, cell towers, companies that want to showcase their company with aerial drone photography

Contact Information for Business Card

logo files have been submitted in pdf, jpg, png, .ai, .eps., .svg formats. Please feel free to be creative with design and colors, possibly a cloud type background
sample attached.
review my website www.bluefinskyworks.com that should help with designing my business card
Services:
-Aerial Videos
-Aerial Photography

Font styles to use
Sans Serif

Colors

Designer to choose colors to be used in the design.

Requirements
Must have
• company logo
• Bluefin Sky Works
• Ray Colton Certified Drone Operator
• 770-519-8462
• bluefinskyworks@mailbox.example
• www.bluefinskywarks.com
• 2716 Marlow Ln, Dunwoody GA 30338
Nice to have
• Please feel free to be creative with design and colors

```html
<!DOCTYPE html>
<html lang="en">
<head>
<meta charset="utf-8">
<title>Bluefin Sky Works – Business Card</title>
<link href="https://fonts.googleapis.com/css2?family=Lato:wght@400;700;900&display=swap" rel="stylesheet">
<style>
  :root {
    --page-bg: #4a4c50;
    --sky-light: #bfe3fb;
    --sky-mid: #52b3ee;
    --sky-deep: #1f8fd9;
    --band-white: #ffffff;
    --ink-dark: #1b1d22;
    --card-black: #131417;
    --brand-blue: #1d74c4;
    --text-light: #d8dadd;
    --text-muted: #c9cbce;
  }
  * { margin: 0; padding: 0; box-sizing: border-box; }
  html, body { width: 1200px; height: 1200px; overflow: hidden; }
  body {
    background: var(--page-bg);
    font-family: "Lato", sans-serif;
    position: relative;
  }
  .card {
    position: absolute;
    left: 120px;
    width: 960px;
    height: 540px;
    border-radius: 28px;
    overflow: hidden;
  }
  .card--front { top: 50px; }
  .card--back { top: 620px; background: var(--card-black); }

  /* Front */
  .sky-photo {
    position: absolute; inset: 0;
    background:
      radial-gradient(ellipse 60% 55% at 25% 5%, rgba(255,255,255,0.75), rgba(255,255,255,0) 70%),
      radial-gradient(ellipse 40% 45% at 85% 35%, rgba(225,242,255,0.85), rgba(225,242,255,0) 70%),
      radial-gradient(ellipse 55% 35% at 20% 95%, rgba(225,242,255,0.8), rgba(225,242,255,0) 70%),
      linear-gradient(160deg, var(--sky-light) 0%, var(--sky-mid) 45%, var(--sky-deep) 100%);
  }
  .brand-mark {
    position: absolute;
    display: flex; align-items: center; gap: 14px;
    font-weight: 900; letter-spacing: 1px;
    white-space: nowrap;
  }
  .brand-mark__dot { border-radius: 50%; flex: none; }
  .card--front .brand-mark {
    left: 0; right: 0; top: 190px; justify-content: center;
    color: var(--band-white); font-size: 58px;
  }
  .card--front .brand-mark__dot { background: var(--band-white); width: 34px; height: 34px; }
  .service-band {
    position: absolute; left: 0; right: 0; top: 360px; height: 64px;
    background: var(--band-white);
    display: flex; align-items: center; justify-content: center; gap: 22px;
    color: var(--ink-dark); font-size: 27px; font-weight: 400;
    white-space: nowrap;
  }

  /* Back */
  .card--back .brand-mark {
    left: 50px; top: 225px; color: var(--brand-blue); font-size: 34px;
  }
  .card--back .brand-mark__dot { background: var(--brand-blue); width: 24px; height: 24px; }
  .separator {
    position: absolute; left: 478px; top: 130px; width: 2px; height: 240px;
    background: linear-gradient(to bottom, rgba(29,116,196,0), var(--brand-blue) 45%, rgba(29,116,196,0));
  }
  .contact-block {
    position: absolute; left: 512px; top: 90px; width: 400px;
    color: var(--text-light); white-space: nowrap;
  }
  .contact-block__name {
    color: var(--brand-blue); font-weight: 900; font-size: 46px; letter-spacing: 0.5px; line-height: 1.1;
  }
  .contact-block__title { font-size: 23px; margin-top: 4px; margin-bottom: 30px; color: var(--text-muted); }
  .contact-list { list-style: none; }
  .contact-list__item {
    display: flex; align-items: center; gap: 12px;
    font-size: 20px; line-height: 1.6; color: #ffffff;
  }
  .contact-list__icon { width: 18px; height: 18px; flex: none; fill: var(--brand-blue); }
  .accent-stripe {
    position: absolute; background: var(--brand-blue);
  }
  .accent-stripe--left { left: 0; width: 660px; bottom: 0; height: 48px; }
  .accent-stripe--right { left: 676px; right: 0; bottom: 60px; height: 40px; }
</style>
</head>
<body>

<section class="card card--front">
  <div class="sky-photo" role="img" aria-label="Bright blue sky with sun rays and white clouds"></div>
  <div class="brand-mark">
    <span class="brand-mark__dot"></span>
    <span class="brand-mark__name">BLUEFIN SKY WORKS</span>
  </div>
  <div class="service-band">
    <span>Aerial Videos</span>
    <span class="service-band__divider">|</span>
    <span>Aerial Photography</span>
    <span class="service-band__divider">|</span>
    <span>Aerial Real Estate Photography</span>
  </div>
</section>

<section class="card card--back">
  <div class="brand-mark">
    <span class="brand-mark__dot"></span>
    <span class="brand-mark__name">BLUEFIN SKY WORKS</span>
  </div>
  <div class="separator"></div>
  <div class="contact-block">
    <h1 class="contact-block__name">RAY COLTON</h1>
    <p class="contact-block__title">Certified Drone Operator</p>
    <ul class="contact-list">
      <li class="contact-list__item">
        <svg class="contact-list__icon" viewBox="0 0 20 20"><path d="M10 1a6 6 0 0 0-6 6c0 4.5 6 12 6 12s6-7.5 6-12a6 6 0 0 0-6-6zm0 8.5A2.5 2.5 0 1 1 10 4.5a2.5 2.5 0 0 1 0 5z"/></svg>
        2716 Marlow Ln, Dunwoody GA 30338
      </li>
      <li class="contact-list__item">
        <svg class="contact-list__icon" viewBox="0 0 20 20"><path d="M5 2l3 4-2 2c1 2.5 3.5 5 6 6l2-2 4 3-2 3C8 17 3 12 2 4z"/></svg>
        770-519-8462
      </li>
      <li class="contact-list__item">
        <svg class="contact-list__icon" viewBox="0 0 20 20"><path d="M2 4h16v12H2z M2 4l8 7 8-7" fill="none" stroke="#1d74c4" stroke-width="2"/></svg>
        bluefinskyworks@mailbox.example
      </li>
      <li class="contact-list__item">
        <svg class="contact-list__icon" viewBox="0 0 20 20"><g fill="none" stroke="#1d74c4" stroke-width="1.6"><circle cx="10" cy="10" r="8"/><ellipse cx="10" cy="10" rx="3.5" ry="8"/><path d="M2 10h16M3.5 6h13M3.5 14h13"/></g></svg>
        www.bluefinskyworks.com
      </li>
    </ul>
  </div>
  <div class="accent-stripe accent-stripe--left"></div>
  <div class="accent-stripe accent-stripe--right"></div>
</section>

</body>
</html>
```